sales site promotion- amber kite fest

We need an advertisement for a facebook & website discount campaign ,we promote a sales site for aquarium products, terrarium and ponds!
The campaign runs from September 20-22/2019
The name of the campaign is related to the fest of the amber kite.
the website is www.zelfa.ro , the name of the site has nothing to do with the products we sell!
We want to make a link between the amber kite fest which is September 22nd and our website!
It can be either the graphics included.

facebook

3377b5
9bcb3c
f78f20
ffc214

• our logo
• I bought some models that can be combined!

```html
<!DOCTYPE html>
<html lang="en">
<head>
<meta charset="utf-8">
<title>Fest of the Amber Kite – Zelfa</title>
<link href="https://fonts.googleapis.com/css2?family=Montserrat:wght@500;700;800&display=swap" rel="stylesheet">
<style>
  :root {
    --paper: #ffffff;
    --leaf: #5cc11a;
    --leaf-dark: #4a9f12;
    --slate: #6d6e70;
    --ocean-deep: #0f2fa8;
    --ocean-mid: #2a5fd8;
    --ocean-light: #4f9ae8;
    --partner-blue: #1b4f9c;
  }
  html, body {
    margin: 0;
    padding: 0;
    width: 1200px;
    height: 1200px;
    overflow: hidden;
    background: var(--paper);
    font-family: "Montserrat", sans-serif;
  }
  .poster {
    position: relative;
    width: 1200px;
    height: 1200px;
    background: var(--paper);
  }
  .heart-frame {
    position: absolute;
    left: 0;
    top: 0;
    width: 1200px;
    height: 760px;
  }
  .event-date {
    position: absolute;
    left: 0;
    width: 1200px;
    text-align: center;
    top: 482px;
    color: var(--leaf);
    font-weight: 800;
    font-size: 62px;
    line-height: 74px;
    letter-spacing: 1px;
  }
  .headline {
    position: absolute;
    left: 0;
    width: 1200px;
    top: 722px;
    margin: 0;
    text-align: center;
    font-weight: 800;
    font-size: 112px;
    line-height: 122px;
    letter-spacing: -2px;
  }
  .headline .line-top { display: block; color: var(--slate); }
  .headline .line-bottom { display: block; color: var(--leaf); }
  .brand-row {
    position: absolute;
    top: 1010px;
    left: 0;
    width: 1200px;
    height: 150px;
  }
  .brand {
    position: absolute;
    display: flex;
    align-items: center;
    gap: 22px;
  }
  .brand-host { left: 60px; top: 20px; }
  .brand-partner { left: 680px; top: 40px; }
  .brand-mark-square {
    width: 86px;
    height: 86px;
    background: var(--leaf);
  }
  .brand-mark-circle {
    width: 84px;
    height: 84px;
    border-radius: 50%;
    background: var(--leaf);
  }
  .brand-host .brand-name {
    font-weight: 700;
    font-size: 84px;
    letter-spacing: 6px;
    color: var(--slate);
    line-height: 1;
  }
  .brand-host .brand-url {
    position: absolute;
    left: 230px;
    top: 112px;
    font-weight: 500;
    font-size: 27px;
    color: var(--slate);
    white-space: nowrap;
  }
  .brand-partner .brand-name {
    font-weight: 800;
    font-size: 70px;
    color: var(--partner-blue);
    line-height: 1;
  }
</style>
</head>
<body>
<main class="poster">
  <svg class="heart-frame" viewBox="0 0 1200 760" aria-hidden="false">
    <defs>
      <clipPath id="heart-inner-clip">
        <path d="M593,178 C560,120 505,90 440,90 C345,90 275,165 275,255 C275,322 318,375 372,430 L593,665 L814,430 C868,375 938,322 938,255 C938,165 868,90 773,90 C690,90 626,120 593,178 Z"/>
      </clipPath>
      <linearGradient id="ocean-fill" x1="0" y1="0" x2="0.6" y2="1">
        <stop offset="0" stop-color="var(--ocean-deep)"/>
        <stop offset="0.55" stop-color="var(--ocean-mid)"/>
        <stop offset="1" stop-color="var(--ocean-light)"/>
      </linearGradient>
    </defs>
    <path class="heart-outline" d="M593,148 C558,88 500,52 430,52 C318,52 240,140 240,252 C240,332 290,392 350,452 L593,706 L836,452 C896,392 974,332 974,252 C974,140 896,52 784,52 C686,52 628,88 593,148 Z"
          fill="none" stroke="var(--leaf)" stroke-width="24" stroke-linejoin="round"/>
    <path d="M593,148 C558,88 500,52 430,52 C318,52 240,140 240,252 C240,332 290,392 350,452 L593,706 L836,452 C896,392 974,332 974,252 C974,140 896,52 784,52 C686,52 628,88 593,148 Z"
          fill="none" stroke="var(--leaf-dark)" stroke-width="4" stroke-linejoin="round" transform="translate(0,6)" opacity="0.5"/>
    <g clip-path="url(#heart-inner-clip)">
      <rect x="240" y="60" width="740" height="401" fill="url(#ocean-fill)"
            role="img" aria-label="Underwater reef photo with tropical fish and a rhino mother and calf silhouette"/>
    </g>
  </svg>

  <div class="event-date">22<br>SEP</div>

  <h1 class="headline">
    <span class="line-top">FEST OF THE</span>
    <span class="line-bottom">AMBER KITE</span>
  </h1>

  <div class="brand-row">
    <div class="brand brand-host">
      <span class="brand-mark-square"></span>
      <span class="brand-name">ZELFA</span>
      <span class="brand-url">www.zelfa.ro</span>
    </div>
    <div class="brand brand-partner">
      <span class="brand-mark-circle"></span>
      <span class="brand-name">NOVAQUA</span>
    </div>
  </div>
</main>
</body>
</html>
```